IT Tradingsystem for car dealers needs Business Card Design

We need a fresh and modern design for our new business cards.

We develop a it-business system for car dealers in Sweden, Norway and on our way down to further countries in Europe, hence the namechange to Brovento Nordic AB. The site can be found at www.brovento.example. The startpage is also in for an update/modernization soon so don't take to much from here.

We are looking to print double sided, 4-colour cards.

We want to look professional, modern and serious. Open to cooler suggestions, but not too crazy. We need to make a good and serious impression on our potential customers. It needs to reflect our scandinavian design values and layout.

Preferably with the full Brovento logo in good size on the back, so the small print on the logo can be read easily.

Text that needs to go on the cards:
-------

Otto Sigurd Hamberg
Founder

Direct +46 70-512 96 44
Support 08-527 93 214
os.hamberg@brovento.example

Brovento Nordic AB
Box 7816
111 48 Stockholm

Brovento.example
Vagnkollen.example

--------
Good luck and thanks!

PS. If you need more input or see what our previous cards looked like, don't hesitate to contact me!

Target Market(s)

Decision makers / executives at brand cardealers

Industry/Entity Type

Automotive

Contact Information for Business Card

Normal size

Requirements
Must have
• Full logo
Nice to have
• Base on our orange colors
Should not have
• No fonts with serif, and not too much graphics

```html
<!DOCTYPE html>
<html lang="en">
<head>
<meta charset="utf-8">
<title>Brovento Nordic AB – Business Card</title>
<link rel="stylesheet" href="https://fonts.googleapis.com/css2?family=Lato:wght@400;700;900&display=swap">
<style>
  :root {
    --backdrop: #3a3a3b;
    --card: #26282a;
    --orange: #f47b20;
    --text-light: #f2f2f2;
    --divider: #d9d9d9;
  }
  * { margin: 0; padding: 0; box-sizing: border-box; }
  html, body {
    width: 1200px; height: 1189px; overflow: hidden;
    background: var(--backdrop);
    font-family: "Lato", Arial, sans-serif;
  }
  .canvas { position: relative; width: 1200px; height: 1189px; }
  .card {
    position: absolute; left: 150px; width: 900px; height: 520px;
    background: var(--card); border-radius: 26px; overflow: hidden;
  }
  .card--front { top: 50px; }
  .card--back { top: 620px; }

  /* Front */
  .front-brand {
    position: absolute; left: 190px; top: 190px;
    display: flex; flex-direction: column;
  }
  .brand-row { display: flex; align-items: center; gap: 24px; }
  .brand-square { width: 64px; height: 64px; background: var(--orange); }
  .brand-name {
    color: var(--text-light); font-weight: 900; font-size: 96px;
    letter-spacing: -1px; line-height: 1;
  }
  .brand-tagline {
    margin-left: 88px; margin-top: 8px;
    color: var(--text-light); font-size: 22px; letter-spacing: 1px;
  }

  /* Back */
  .back-brand {
    position: absolute; left: 60px; top: 0; width: 360px; height: 520px;
    display: flex; align-items: center; justify-content: center; gap: 16px;
  }
  .back-brand .brand-square { width: 44px; height: 44px; }
  .back-brand .brand-name { color: var(--orange); font-size: 56px; }
  .divider {
    position: absolute; left: 440px; top: 70px; width: 2px; height: 380px;
    background: var(--divider);
  }
  .contact {
    position: absolute; left: 490px; top: 78px;
    color: var(--text-light); font-size: 22px; line-height: 1.25;
  }
  .contact-name { font-weight: 700; font-size: 27px; }
  .contact-role { color: var(--orange); font-size: 22px; margin-bottom: 18px; }
  .contact-block { margin-bottom: 18px; }
  .label { color: var(--orange); }
</style>
</head>
<body>
<main class="canvas">
  <section class="card card--front" aria-label="Card front">
    <div class="front-brand">
      <div class="brand-row">
        <span class="brand-square" aria-hidden="true"></span>
        <span class="brand-name">Brovento</span>
      </div>
      <p class="brand-tagline">Bruktest | Remarketing | vagnkollen.example</p>
    </div>
  </section>

  <section class="card card--back" aria-label="Card back">
    <div class="back-brand">
      <span class="brand-square" aria-hidden="true"></span>
      <span class="brand-name">Brovento</span>
    </div>
    <div class="divider" aria-hidden="true"></div>
    <div class="contact">
      <p class="contact-name">Otto Sigurd Hamberg</p>
      <p class="contact-role">Founder</p>
      <div class="contact-block">
        <p>Brovento Nordic AB</p>
        <p>Box 7816</p>
        <p>111 48 Stockholm</p>
      </div>
      <div class="contact-block">
        <p><span class="label">Direct:</span> +46 70-512 96 44</p>
        <p><span class="label">Support</span> 08-527 93 214</p>
        <p><span class="label">Email:</span> os.hamberg@brovento.example</p>
      </div>
      <div class="contact-block">
        <p><span class="label">Brovento</span>.example</p>
        <p>Vagnkollen.example</p>
      </div>
    </div>
  </section>
</main>
</body>
</html>
```